Haus 736 AG (real estate company)

We need a letter design including a logo for our newly founded Haus 736 AG. Haus 736 AG is a real estate company that buys and manages real estate and energy production systems such as photovoltaic systems. The number 736 in the name of the AG comes from the fact that the insurance number of the first property to be purchased has this number.
Updates
Ich brauche zusätzliche Tage um durchzusehen
Target Market(s)
tenants of business premises
Industry/Entity Type
Immobilien
Font styles to use
- Arial
Look and feel

```html
<!DOCTYPE html>
<html lang="en">
<head>
<meta charset="utf-8">
<title>Haus 736 AG – Stationery</title>
<link rel="stylesheet" href="https://fonts.googleapis.com/css2?family=Arimo:wght@400&family=Montserrat:wght@400;500;700&display=swap">
<style>
  :root {
    --navy: #1f3b6f;
    --sage: #849589;
    --body-grey: #7b7b7b;
    --paper: #ffffff;
    --page-bg: #ffffff;
    --shadow: 5px 5px 9px rgba(0, 0, 0, 0.32);
  }
  * { box-sizing: border-box; margin: 0; padding: 0; }
  html, body {
    width: 1200px; height: 980px; overflow: hidden;
    background: var(--page-bg);
  }
  .canvas { position: relative; width: 1200px; height: 980px; }

  .wordmark {
    position: absolute; display: flex; align-items: center;
    font-family: "Montserrat", sans-serif; font-weight: 500;
    color: var(--navy); white-space: nowrap; letter-spacing: -0.02em;
  }
  .wordmark-square { background: var(--navy); flex: none; }

  /* Letter */
  .letter {
    position: absolute; left: 62px; top: 83px; width: 649px; height: 839px;
    background: var(--paper); box-shadow: var(--shadow);
  }
  .letter .wordmark { left: 110px; top: 30px; font-size: 48px; line-height: 58px; }
  .letter .wordmark-square { width: 52px; height: 52px; margin-right: 14px; }

  .sender {
    position: absolute; left: 111px; top: 138px;
    font-family: "Montserrat", sans-serif; color: var(--sage);
  }
  .sender-name { font-size: 17px; font-weight: 500; line-height: 22px; margin-bottom: 7px; letter-spacing: 0.01em; }
  .sender-line { font-size: 12.4px; line-height: 16px; letter-spacing: 0.02em; }
  .letter-date {
    position: absolute; right: 87px; top: 214px;
    font-family: "Montserrat", sans-serif; font-size: 12.4px; line-height: 16px;
    color: var(--sage); letter-spacing: 0.02em;
  }

  .letter-body {
    position: absolute; left: 110px; top: 266px; width: 455px;
    font-family: "Arimo", Arial, sans-serif; font-size: 9.4px; line-height: 17px;
    color: var(--body-grey);
  }
  .letter-body p { margin-bottom: 17px; }
  .letter-body p.tight { margin-bottom: 12px; }
  .letter-body .salutation { margin-bottom: 17px; }

  .closing {
    position: absolute; left: 110px; top: 655px;
    font-family: "Arimo", Arial, sans-serif; font-size: 9.4px; line-height: 17px; color: var(--body-grey);
  }
  .signatory { position: absolute; left: 107px; top: 690px; font-family: "Montserrat", sans-serif; color: var(--sage); }
  .signatory-name { font-size: 15.5px; font-weight: 500; line-height: 20px; letter-spacing: 0.02em; }
  .signatory-role { font-size: 12.4px; line-height: 16px; margin-top: 2px; letter-spacing: 0.03em; }

  .footer-rule { position: absolute; left: 110px; top: 768px; width: 430px; height: 3px; background: var(--sage); }
  .footer-contact {
    position: absolute; left: 110px; top: 774px;
    font-family: "Montserrat", sans-serif; font-size: 15.5px; line-height: 19px; color: var(--navy);
  }

  /* Business cards */
  .card {
    position: absolute; left: 785px; width: 267px; height: 153px;
    background: var(--paper); box-shadow: var(--shadow);
  }
  .card-front { top: 82px; }
  .card-back { top: 281px; }
  .card .wordmark { left: 27px; font-size: 30px; line-height: 36px; }
  .card .wordmark-square { width: 34px; height: 34px; margin-right: 9px; }
  .card-front .wordmark { top: 21px; }
  .card-back .wordmark { top: 58px; }

  .card-name {
    position: absolute; left: 0; width: 100%; top: 151px; top: 69px; text-align: center;
    font-family: "Montserrat", sans-serif; font-weight: 700; font-size: 19.5px; line-height: 24px;
    color: var(--navy); letter-spacing: -0.02em;
  }
  .card-role {
    position: absolute; left: 0; width: 100%; top: 91px; text-align: center;
    font-family: "Montserrat", sans-serif; font-weight: 700; font-size: 9.5px; line-height: 12px;
    color: var(--navy); letter-spacing: 0.3em; padding-left: 0.3em;
  }
  .card-contact {
    position: absolute; right: 9px; top: 111px; text-align: right;
    font-family: "Montserrat", sans-serif; font-weight: 700; font-size: 7.4px; line-height: 9.6px;
    color: var(--body-grey);
  }
</style>
</head>
<body>
<main class="canvas">

  <article class="letter">
    <div class="wordmark"><span class="wordmark-square"></span>Haus 736 AG</div>

    <address class="sender" style="font-style: normal;">
      <div class="sender-name">Name Surname</div>
      <div class="sender-line">Senior Executive</div>
      <div class="sender-line">Address. Street, City, Country</div>
      <div class="sender-line">contact@mail.com</div>
      <div class="sender-line">000-999-888-777</div>
    </address>
    <div class="letter-date">Date, 29 September, 2022</div>

    <div class="letter-body">
      <p class="salutation">Dear Mr Keller,</p>
      <p>Lorem ipsum dolor sit amet, consectetuer adipiscing elit, sed diam nonummy nibh euismod tincidunt ut laoreet dolore magna aliquam erat volutpat. Ut wisi enim ad minim veniam, quis nostrud exerci tation ullam-corper.</p>
      <p class="tight">Et iusto odio dignissim qui blandit praesent luptatum zzril delenit augue duis dolore te feugait nulla facilisi. Lorem ipsum dolor sit amet, consectetuer adipiscing elit, sed diam nonummy nibh euismod tincidunt ut laoreet dolore magna aliquam erat volutpat. Ut wisi enim ad minim veniam, quis exerci tation ullamcorper</p>
      <p>Duis autem vel eum iriure dolor in hendrerit in vulputate velit esse molestie consequat, vel illum dolore eu feugiat nulla facilisis at vero eros et accumsan et iusto odio dignissim qui blandit praesent luptatum zzril delenit augue duis dolore te feugait nulla facilisi. Nam liber tempor cum soluta nobis eleifend option congue nihil imperdiet doming id quod mazim placerat facer wisi enim ad minim veniam possim assum.</p>
      <p>Lorem ipsum dolor sit amet, consectetuer adipiscing elit, sed diam nonummy nibh minim veniam, quis nos-trud exerci tation ullamcorper suscipit lobortis nisl ut aliquip ex ea commodo consequat.</p>
      <p>Duis autem vel eum iriure dolor in hendrerit in vulputate velit esse molestieet iusto euismod tincidunt ut laoreet dolore magna aliquam erat volutpat. Ut wisi enim ad odio dignissim qui blandit praesent.</p>
    </div>

    <div class="closing">Yours Sincerely,</div>
    <div class="signatory">
      <div class="signatory-name">NAME SURNAME</div>
      <div class="signatory-role">General Manager</div>
    </div>

    <div class="footer-rule"></div>
    <div class="footer-contact">
      <div>Haus 736 AG, Lindenweg 12, 8000 Musterdorf</div>
      <div>Tel. 079 000 12 34</div>
      <div>info@haus-736.ch</div>
    </div>
  </article>

  <section class="card card-front">
    <div class="wordmark"><span class="wordmark-square"></span>Haus 736 AG</div>
    <div class="card-name">Name Surname</div>
    <div class="card-role">MENAGER</div>
    <div class="card-contact">
      <div>Phone: 079 000 12 34</div>
      <div>info@haus-736.ch</div>
      <div>Address: Lindenweg 12, 8000 Musterdorf</div>
    </div>
  </section>

  <section class="card card-back">
    <div class="wordmark"><span class="wordmark-square"></span>Haus 736 AG</div>
  </section>

</main>
</body>
</html>
```